Brill Insurance Agency - Business Cards

Hello, I am needing new trendy business cards for our Insurance Agency now that I have a new Logo. I have attached our new logo with several color options along with a business card design that I like. I am leaning towards burgundy and blue colors. I have attached our current business card. I have also attached a headshot of our company president, Martin Vale, that you can use if you wish. Thank you so much in advance for all the wonderful designs!!!!

Target Market(s)

We want to look very professional to potential customers and we also want to look very professional so insurance companies will want to contract with us to sell their product.

Industry/Entity Type

Insurance

Contact Information for Business Card

Martin Vale
mvale@brillagency.com
Business: 555-213-4087
Fax: 555-213-7751
Cell: 555-390-2618
Toll Free: 888-555-0194
42 W Elm Rd Butler, MO 64730
www.brillagency.net

Font styles to use
Serif
Sans Serif

Colors
0355a3
3277b5
f04a50
ec1f27

Requirements
Nice to have
• I love creativity. The more creative and balanced a business card design the more I will like it. I would like the card to be printed horizontally instead of vertically.
Should not have
• My project should not have the Allied Coverage Network logo. It is no longer used in the industry.

```html
<!DOCTYPE html>
<html lang="en">
<head>
<meta charset="utf-8">
<title>Brill Insurance Agency – Business Cards</title>
<link rel="stylesheet" href="https://fonts.googleapis.com/css2?family=Montserrat:wght@400;500;700&family=Dancing+Script:wght@500&display=swap">
<style>
  :root {
    --blue: #0355a3;
    --blue-light: #3277b5;
    --red: #ec1f27;
    --red-soft: #f04a50;
    --white: #ffffff;
    --ink: #3a3a3a;
    --page: #efefef;
    --mark-faint: rgba(255,255,255,0.4);
  }
  * { box-sizing: border-box; margin: 0; padding: 0; }
  html, body { width: 1200px; height: 1086px; overflow: hidden; }
  body { background: var(--page); font-family: "Montserrat", sans-serif; position: relative; }

  .card {
    position: absolute; width: 560px; height: 311px; overflow: hidden;
    background: var(--blue); box-shadow: 0 4px 14px rgba(0,0,0,0.18);
  }
  .card--front-a { left: 30px; top: 170px; }
  .card--front-b { left: 610px; top: 170px; }
  .card--back { left: 320px; top: 560px; }

  .card__top { position: absolute; left: 0; top: 0; width: 100%; height: 156px; background: var(--white); border-bottom: 4px solid var(--red); }

  .brand { position: absolute; left: 28px; top: 26px; display: flex; align-items: center; white-space: nowrap; }
  .brand__dot { width: 46px; height: 46px; border-radius: 50%; border: 5px solid var(--red); flex: none; }
  .brand__rule { width: 2px; height: 58px; background: #555; margin: 0 12px; flex: none; }
  .brand__name { color: var(--blue); font-weight: 700; font-size: 23px; letter-spacing: 0.2px; line-height: 1; }
  .brand__sub {
    display: flex; align-items: center; gap: 6px; margin-top: 4px;
    color: var(--ink); font-weight: 700; font-size: 11px; letter-spacing: 3.5px;
  }
  .brand__sub::before, .brand__sub::after { content: ""; flex: 1; height: 1.5px; background: var(--ink); }

  .person { position: absolute; left: 32px; top: 112px; display: flex; align-items: center; white-space: nowrap; }
  .person__name { font-family: "Dancing Script", cursive; font-size: 28px; color: #444; }
  .person__rule { width: 1px; height: 20px; background: #666; margin: 0 10px; }
  .person__role { font-size: 10.5px; letter-spacing: 0.5px; color: #444; }

  .contacts { position: absolute; left: 30px; top: 172px; list-style: none; }
  .contacts li { display: flex; align-items: center; height: 18px; color: var(--white); font-size: 12.5px; white-space: nowrap; }
  .contacts svg { width: 14px; height: 14px; margin-right: 14px; flex: none; }

  .photo { position: absolute; }
  .photo--rect {
    right: 22px; top: 40px; width: 180px; height: 166px;
    background: linear-gradient(180deg, #eef0f4 0%, #d7b8a6 45%, #2a2d36 75%, #15171c 100%);
    border-radius: 90px 90px 0 0;
  }
  .photo--round {
    right: 22px; top: 60px; width: 190px; height: 190px; border-radius: 50%;
    border: 4px solid var(--red);
    background: linear-gradient(180deg, #eef0f4 0%, #d7b8a6 45%, #2a2d36 72%, #15171c 100%);
  }

  .back-brand { position: absolute; left: 50%; top: 50%; transform: translate(-50%, -50%); display: flex; align-items: center; white-space: nowrap; }
  .back-brand .brand__dot { width: 70px; height: 70px; border: 7px solid var(--red-soft); }
  .back-brand .brand__rule { height: 86px; background: var(--mark-faint); margin: 0 16px; }
  .back-brand .brand__name { color: var(--mark-faint); font-size: 27px; }
  .back-brand .brand__sub { color: var(--mark-faint); font-size: 13px; letter-spacing: 5px; }
  .back-brand .brand__sub::before, .back-brand .brand__sub::after { background: var(--mark-faint); }
</style>
</head>
<body>

<svg width="0" height="0" style="position:absolute">
  <defs>
    <symbol id="ic-mail" viewBox="0 0 16 16"><circle cx="8" cy="8" r="7" fill="none" stroke="#fff" stroke-width="1.2"/><rect x="4" y="5.5" width="8" height="5" fill="none" stroke="#fff"/><path d="M4 5.5 8 8.5 12 5.5" fill="none" stroke="#fff"/></symbol>
    <symbol id="ic-phone" viewBox="0 0 16 16"><circle cx="8" cy="8" r="7" fill="none" stroke="#fff" stroke-width="1.2"/><path d="M5.5 4.5c-.8.8 0 3 1.8 4.8s4 2.6 4.8 1.8l-1.3-1.4-1.2.7c-1-.5-1.8-1.3-2.3-2.3l.7-1.2z" fill="#fff"/></symbol>
    <symbol id="ic-home" viewBox="0 0 16 16"><circle cx="8" cy="8" r="7" fill="none" stroke="#fff" stroke-width="1.2"/><path d="M4.5 8 8 5l3.5 3v3.5h-7z" fill="#fff"/></symbol>
    <symbol id="ic-web" viewBox="0 0 16 16"><circle cx="8" cy="8" r="7" fill="none" stroke="#fff" stroke-width="1.2"/><circle cx="8" cy="8" r="3.8" fill="none" stroke="#fff"/><path d="M4.2 8h7.6M8 4.2v7.6" stroke="#fff"/></symbol>
    <symbol id="ic-pin" viewBox="0 0 16 16"><circle cx="8" cy="8" r="7" fill="none" stroke="#fff" stroke-width="1.2"/><path d="M8 12s-3-3-3-5a3 3 0 0 1 6 0c0 2-3 5-3 5z" fill="#fff"/><circle cx="8" cy="7" r="1" fill="#0355a3"/></symbol>
  </defs>
</svg>

<section class="card card--front-a">
  <div class="card__top"></div>
  <div class="brand">
    <span class="brand__dot"></span><span class="brand__rule"></span>
    <div><div class="brand__name">BRILL INSURANCE</div><div class="brand__sub">AGENCY INC</div></div>
  </div>
  <div class="person"><span class="person__name">Martin Vale</span><span class="person__rule"></span><span class="person__role">INSURANCE BROKER</span></div>
  <div class="photo photo--rect" role="img" aria-label="Headshot of Martin Vale in a dark suit and red tie"></div>
  <ul class="contacts">
    <li><svg><use href="#ic-mail"/></svg>mvale@brillagency.com</li>
    <li><svg><use href="#ic-phone"/></svg>555-213-4087 | ext 23</li>
    <li><svg><use href="#ic-phone"/></svg>555-213-7751</li>
    <li><svg><use href="#ic-home"/></svg>555-390-2618</li>
    <li><svg><use href="#ic-phone"/></svg>888-555-0194</li>
    <li><svg><use href="#ic-web"/></svg>www.brillagency.net</li>
    <li><svg><use href="#ic-pin"/></svg>42 W Elm Rd Butler, MO 64730</li>
  </ul>
</section>

<section class="card card--front-b">
  <div class="card__top"></div>
  <div class="brand">
    <span class="brand__dot"></span><span class="brand__rule"></span>
    <div><div class="brand__name">BRILL INSURANCE</div><div class="brand__sub">AGENCY INC</div></div>
  </div>
  <div class="person"><span class="person__name">Martin Vale</span><span class="person__rule"></span><span class="person__role">INSURANCE BROKER</span></div>
  <div class="photo photo--round" role="img" aria-label="Round headshot of Martin Vale in a dark suit and red tie"></div>
  <ul class="contacts">
    <li><svg><use href="#ic-mail"/></svg>mvale@brillagency.com</li>
    <li><svg><use href="#ic-phone"/></svg>555-213-4087 | ext 23</li>
    <li><svg><use href="#ic-phone"/></svg>555-213-7751</li>
    <li><svg><use href="#ic-home"/></svg>555-390-2618</li>
    <li><svg><use href="#ic-phone"/></svg>888-555-0194</li>
    <li><svg><use href="#ic-web"/></svg>www.brillagency.net</li>
    <li><svg><use href="#ic-pin"/></svg>42 W Elm Rd Butler, MO 64730</li>
  </ul>
</section>

<section class="card card--back">
  <div class="back-brand">
    <span class="brand__dot"></span><span class="brand__rule"></span>
    <div><div class="brand__name">BRILL INSURANCE</div><div class="brand__sub">AGENCY INC</div></div>
  </div>
</section>

</body>
</html>
```